Geschäftspapiere für Rechtsanwaltskanzlei
Zielgruppe
Rechtsanwaltskanzlei
Aufgabenstellung
Bitte inklusive Logo (sollte Recht, Digital/Apps, Medizin illustrieren) - habe das Preisgeld vor diesem Hintergrund erhöht.
Die Kanzlei arbeitet an der Schnittstelle von (Medizin-)Recht und Digital. Von daher wären wären Symbole/Gestaltung aus Bereich Medizin, Recht und Digital (z.B. Apps etc.) passend.
Das Briefpapier soll alle wichtigen Infos enthalten, aber dabei sehr klar gehalten werden und nicht überladen sein. Mir ist ein schlichtes und ansprechendes Design wichtig. Es soll nicht verspielt sein.
Info auf Briefpapier:
Kanzlei für Medizinrecht
Rechtsanwalt Dr. Lukas Brandl - Fachanwalt für Medizinrecht
Bitte Platzhalter/Freitextfelder für die anderen anderen Angaben, wie:
- Adresse
- Telefon-Nr.
- Homepage
- E-Mail
- Bankdaten.

```html
<!DOCTYPE html>
<html lang="de">
<head>
<meta charset="utf-8">
<title>Geschäftspapiere – Dr. Lukas Brandl Rechtsanwälte</title>
<link rel="stylesheet" href="https://fonts.googleapis.com/css2?family=Playfair+Display+SC:wght@700&family=Questrial&family=Montserrat:wght@500;600&display=swap">
<style>
  :root {
    --board: #383838;
    --paper: #ffffff;
    --envelope: #efeff1;
    --ink: #4a3b26;
    --band: #958a74;
    --flap-line: #9a9a9a;
    --serif: "Playfair Display SC", Georgia, serif;
    --sans: "Questrial", "Helvetica Neue", Arial, sans-serif;
    --small: "Montserrat", Arial, sans-serif;
  }
  * { box-sizing: border-box; margin: 0; padding: 0; }
  html, body { width: 1200px; height: 840px; overflow: hidden; background: var(--board); }
  .board { position: relative; width: 1200px; height: 840px; }

  .sheet { position: absolute; box-shadow: 3px 4px 6px rgba(0,0,0,.45); }

  /* Letterhead */
  .letterhead { left: 51px; top: 72px; width: 503px; height: 712px; background: var(--paper); }
  .letterhead .side-bar { position: absolute; right: 0; top: 35px; width: 9px; height: 142px; background: var(--band); }
  .letterhead .foot-band { position: absolute; left: 0; right: 0; bottom: 8px; height: 6px; background: var(--band); }
  .letterhead .fold-mark { position: absolute; left: 8px; top: 485px; width: 10px; height: 1px; background: var(--ink); }
  .letterhead .lockup { position: absolute; left: 47px; top: 27px; font-size: 16.5px; }

  .contact { position: absolute; left: 376px; top: 35px; font-family: var(--small); font-style: normal; font-weight: 600; font-size: 7px; line-height: 12px; color: var(--ink); white-space: nowrap; }
  .contact .label { display: inline-block; width: 21px; }
  .contact .divider { width: 60px; height: 1px; background: var(--ink); opacity: .6; margin: 8px 0 10px 18px; }

  /* Logo lockup */
  .lockup { display: flex; align-items: center; gap: .55em; color: var(--ink); }
  .lockup .mark { width: 3em; height: 3em; border: .07em solid var(--ink); flex: none; }
  .lockup .words { display: flex; flex-direction: column; align-items: stretch; }
  .lockup .name { font-family: var(--serif); font-weight: 700; font-size: 1em; line-height: 1.05; white-space: nowrap; }
  .lockup .firm { display: flex; align-items: center; gap: .4em; font-family: var(--sans); font-size: .42em; letter-spacing: .14em; line-height: 1.3; }
  .lockup .firm::before, .lockup .firm::after { content: ""; flex: 1; height: 1px; background: var(--ink); }
  .lockup .tagline { font-family: var(--sans); font-size: .62em; white-space: nowrap; line-height: 1.4; }

  /* Logo card */
  .logo-card { left: 641px; top: 72px; width: 494px; height: 159px; background: var(--paper); display: flex; align-items: center; justify-content: center; }
  .logo-card .lockup { font-size: 36px; gap: .4em; }

  /* Envelopes */
  .envelope { background: var(--envelope); }
  .envelope-back { left: 642px; top: 267px; width: 492px; height: 248px; }
  .envelope-back svg { position: absolute; inset: 0; }
  .envelope-back .sender { position: absolute; left: 0; right: 0; top: 30px; text-align: center; color: var(--ink); }
  .envelope-back .sender-name { font-family: var(--serif); font-weight: 700; font-size: 20px; }
  .envelope-back .sender-address { font-family: var(--sans); font-size: 12.5px; margin-top: 38px; letter-spacing: .02em; }
  .envelope-front { left: 643px; top: 536px; width: 496px; height: 248px; }
  .envelope-front .lockup { position: absolute; left: 231px; top: 155px; font-size: 16.5px; }
</style>
</head>
<body>
<main class="board">

  <section class="sheet letterhead" aria-label="Briefbogen">
    <div class="lockup">
      <span class="mark"></span>
      <div class="words">
        <span class="name">Dr. Lukas Brandl</span>
        <span class="firm">RECHTSANWÄLTE</span>
        <span class="tagline">Fachanwalt für Medizinrecht</span>
      </div>
    </div>

    <address class="contact">
      <div>KONTAKT</div>
      <div><span class="label">Tel.</span> +49 000 000 47 3380</div>
      <div><span class="label">Fax.</span> +49 000 000 47 3381</div>
      <div><span class="label">Mail.</span> info@kanzlei-bsp.de</div>
      <div><span class="label">Web.</span> www.kanzlei-bsp.de</div>
      <div class="divider"></div>
      <div>Bank: Sparkasse Rheintal</div>
      <div>IBAN: DE XX 12345XX 0000004711</div>
      <div>BIC-Swift: MSTRDE00XXX</div>
      <div>Amtsgericht Musterstadt</div>
      <div>Handelsregister: 0000789</div>
      <div>USt.-ID-Nr.: DE0007890000</div>
    </address>

    <span class="side-bar"></span>
    <span class="fold-mark"></span>
    <span class="foot-band"></span>
  </section>

  <section class="sheet logo-card" aria-label="Logo">
    <div class="lockup">
      <span class="mark"></span>
      <div class="words">
        <span class="name">Dr. Lukas Brandl</span>
        <span class="firm">RECHTSANWÄLTE</span>
        <span class="tagline">Fachanwalt für Medizinrecht</span>
      </div>
    </div>
  </section>

  <section class="sheet envelope envelope-back" aria-label="Briefumschlag Rückseite">
    <svg width="492" height="248" viewBox="0 0 492 248" aria-hidden="true">
      <polyline points="14,22 246,175 490,4" fill="none" stroke="#c4c4c6" stroke-width="5" stroke-linejoin="round" transform="translate(2,3)"/>
      <polyline points="14,22 246,175 490,4" fill="none" stroke="var(--flap-line)" stroke-width="1.6" stroke-linejoin="round"/>
    </svg>
    <div class="sender">
      <div class="sender-name">Dr. Lukas Brandl</div>
      <div class="sender-address">AM KASTANIENWEG 18, 46050</div>
    </div>
  </section>

  <section class="sheet envelope envelope-front" aria-label="Briefumschlag Vorderseite">
    <div class="lockup">
      <span class="mark"></span>
      <div class="words">
        <span class="name">Dr. Lukas Brandl</span>
        <span class="firm">RECHTSANWÄLTE</span>
        <span class="tagline">Fachanwalt für Medizinrecht</span>
      </div>
    </div>
  </section>

</main>
</body>
</html>
```